We need a PowerPoint to outline what Modeling is about!

PowerPoint presentation to be shown to aspiring models. The students will be joining our 1-day workshop, and they will be taught the very basics of being a model.
What should be included in the slides:
• What is Modelling? - Description of Modelling, and what it takes to be a Model.
• Types of Models in the market - Catwalk Model / Photography Model / Events Model
• Expectations of a model - Professionalism, Punctuality, Confidence, etc etc.
• Practical (catwalk) tips: Posture
• Practical (catwalk) tips: How to do a simple catwalk
• Practical (photography) tips: How to bring out your best angles in photos
• Trainer Assessment of Students
Here are some definitions that we use. You may change the wording as you see fit, as long as the meaning is the same.
Modelling is to promote a product / brand / service in an advertisement, show, commercial or event.
Runway / Fashion Model – Walk the catwalk to promote clothing and accessories in a fashion show.
Most shows require the model to be tall and skinny. Model needs to strut with confidence and grace down the runway. Body shape more important than facial features.
Photography Model – Appear for Print Ads, Magazine Editorials, Posters, etc.
Height requirements are not as strict (or not present) as compared to Runway Model. Good features preferred, but not a must.
Video Model – Appear for TV commercials, Promotional Videos, etc.
Model needs to possess basic acting skills to promote the product, brand or service on video. Confidence and screen charisma more important than looks or body.
Events Model – Promote the product, brand or service during ‘live’ events and shows.
Model needs to be engaging and charismatic to ‘sell’ the product to customers.
A longer description can also be found here: http://www.brightlarkagency.sg/models/
Target Market(s)
Adults aged 18 - 40 who are interested to take up Modeling.
Industry/Entity Type
Events
Requirements
Must have
- Visually appealing! Does not have to be content heavy, but should deliver the message effectively.
Nice to have
- Pretty pictures.

```html
<!DOCTYPE html>
<html lang="en">
<head>
<meta charset="utf-8">
<title>Bright Lark Agency – Modelling Workshop Slides</title>
<link href="https://fonts.googleapis.com/css2?family=Open+Sans:wght@400;600;700&display=swap" rel="stylesheet">
<style>
  :root {
    --board: #2b2b2b;
    --slide: #ffffff;
    --band: #3a3a3a;
    --ink: #2e2e2e;
    --rule: #bdbdbd;
    --logo-bg: #333333;
    --logo-ink: #ffffff;
    --photo-dark: #9e9e9e;
    --photo-mid: #c9c9c9;
    --photo-light: #e8e8e8;
  }
  * { margin: 0; padding: 0; box-sizing: border-box; }
  html, body { width: 1200px; height: 1000px; overflow: hidden; }
  body {
    background: var(--board);
    font-family: "Open Sans", Verdana, sans-serif;
    color: var(--ink);
    position: relative;
  }
  .slide { position: absolute; background: var(--slide); overflow: hidden; }
  .slide--title { left: 20px; top: 46px; width: 566px; height: 424px; }
  .slide--types { left: 612px; top: 46px; width: 564px; height: 424px; }
  .slide--what  { left: 20px; top: 551px; width: 566px; height: 424px; }
  .slide--thanks{ left: 620px; top: 556px; width: 568px; height: 426px; }

  .slide__header {
    position: absolute; left: 0; top: 0; right: 0; height: 47px;
    background: var(--band); color: #fff;
    font-size: 23px; letter-spacing: 0.5px;
    padding: 9px 0 0 9px;
  }
  .rules { position: absolute; left: 0; right: 0; height: 26px; z-index: 1; }
  .rules::before, .rules::after {
    content: ""; position: absolute; left: 0; right: 0; height: 2px; background: var(--rule);
  }
  .rules::before { top: 0; }
  .rules::after { bottom: 0; }

  .logo {
    position: absolute; background: var(--logo-bg); color: var(--logo-ink);
    display: flex; align-items: center; justify-content: center; text-align: center;
    font-weight: 400; line-height: 1.15; z-index: 2;
  }
  .slide--title .logo { left: 233px; top: 0; width: 119px; height: 120px; font-size: 22px; }
  .slide--types .logo,
  .slide--what .logo { width: 72px; height: 72px; font-size: 13px; bottom: 0; }
  .slide--types .logo { left: 248px; }
  .slide--what .logo { left: 249px; }
  .slide--thanks .logo { left: 233px; bottom: 0; width: 120px; height: 120px; font-size: 22px; }

  .photo-area { position: absolute; }
  .slide--title .photo-area {
    left: 0; top: 0; width: 300px; height: 424px;
    background:
      radial-gradient(ellipse 38% 22% at 32% 85%, var(--photo-dark) 0%, rgba(158,158,158,0) 100%),
      radial-gradient(ellipse 30% 12% at 40% 52%, #b4b4b4 0%, rgba(180,180,180,0) 100%),
      radial-gradient(ellipse 60% 45% at 30% 60%, var(--photo-mid) 0%, rgba(201,201,201,0) 100%),
      radial-gradient(ellipse 70% 40% at 35% 15%, #f7f7f7 0%, rgba(247,247,247,0) 100%),
      linear-gradient(90deg, #d2d2d2 0%, var(--photo-light) 55%, rgba(255,255,255,0) 100%);
  }
  .slide--title .headline {
    position: absolute; left: 252px; top: 232px;
    font-size: 41px; font-weight: 400; letter-spacing: 1px; color: #333; z-index: 2;
  }

  .type-title { position: absolute; left: 25px; top: 94px; font-size: 21px; line-height: 28px; white-space: nowrap; }
  .type-body { position: absolute; left: 30px; top: 210px; font-size: 16.5px; line-height: 22px; white-space: nowrap; }

  .definition { position: absolute; left: 57px; top: 152px; font-size: 21px; line-height: 27px; white-space: nowrap; }

  .slide--thanks .photo-area {
    left: 0; top: 47px; width: 568px; height: 379px;
    background:
      radial-gradient(ellipse 10% 45% at 20% 45%, #dadada 0%, rgba(218,218,218,0) 100%),
      radial-gradient(ellipse 10% 45% at 50% 45%, #d6d6d6 0%, rgba(214,214,214,0) 100%),
      radial-gradient(ellipse 10% 45% at 82% 45%, #d8d8d8 0%, rgba(216,216,216,0) 100%),
      linear-gradient(180deg, #eaeaea 0%, #f6f6f6 50%, #ededed 100%);
  }
  .contact { position: absolute; font-size: 14.5px; color: #333; z-index: 1; white-space: nowrap; }
  .contact h2 { font-size: 21px; font-weight: 700; line-height: 26px; }
  .contact h3 { font-size: 13.5px; font-weight: 700; line-height: 15px; margin-top: 24px; }
  .contact .lines { margin-top: 10px; line-height: 17px; }
  .contact .small { font-size: 13.5px; line-height: 15px; }
  .contact--find { left: 43px; top: 102px; }
  .contact--call { left: 287px; top: 102px; }
  .contact--call .small { margin-top: 23px; }

  .social { position: absolute; bottom: 10px; display: flex; align-items: center; gap: 4px; font-size: 6.5px; line-height: 1.1; color: #444; z-index: 1; }
  .social__dot { width: 20px; height: 20px; border-radius: 50%; background: #8a8a8a; }
  .social--one { left: 355px; }
  .social--two { left: 428px; }
  .social--three { left: 500px; }
</style>
</head>
<body>

<section class="slide slide--title">
  <div class="photo-area" role="img" aria-label="Black and white close-up portrait of a model with a platinum blonde bob"></div>
  <div class="rules" style="top:32px;left:0;right:auto;width:222px"></div>
  <div class="rules" style="top:32px;left:362px"></div>
  <div class="logo">BRIGHT<br>LARK<br>AGENCY</div>
  <h1 class="headline">PRESENTATION</h1>
</section>

<section class="slide slide--types">
  <div class="slide__header">TYPES OF THE MODELS IN THE MARKET</div>
  <p class="type-title"><strong>Runway / Fashion Model</strong> – Walk the<br>catwalk to promote clothing and accessories<br>in a fashion show.</p>
  <p class="type-body">Most shows require the model to be tall and skinny.<br>Model needs to strut with confidence and grace down<br>the runway. Body shape more important than facial<br>features.</p>
  <div class="rules" style="top:372px;left:0;right:auto;width:240px"></div>
  <div class="rules" style="top:372px;left:328px"></div>
  <div class="logo">BRIGHT<br>LARK<br>AGENCY</div>
</section>

<section class="slide slide--what">
  <div class="slide__header">WHAT IS MODELLING?</div>
  <p class="definition"><strong>Modelling</strong> is to promote a product /<br>brand / service in an advertisement,<br>show, commercial or event.</p>
  <div class="rules" style="top:372px;left:0;right:auto;width:241px"></div>
  <div class="rules" style="top:372px;left:329px"></div>
  <div class="logo">BRIGHT<br>LARK<br>AGENCY</div>
</section>

<section class="slide slide--thanks">
  <div class="slide__header">THANK YOU</div>
  <div class="photo-area" role="img" aria-label="Faded black and white photo of three female models posing in dresses and boots"></div>
  <div class="contact contact--find">
    <h2>Find Us!</h2>
    <p class="lines">27 Larkspur Road #03-11<br>Singapore 418902</p>
    <h3>BRIGHT LARK in the STUDIO</h3>
    <p class="small">For general enquiries,<br>hello@brightlarkagency.sg<br>For bookings,<br>mei@brightlarkagency.sg</p>
  </div>
  <div class="contact contact--call">
    <h2>Call Us!</h2>
    <p class="lines">Tel: +65 6210 4480 (Office Hours)<br>Mobile: +65 9182 3307 (After Hours)<br>Fax: +65 6210 4481</p>
    <p class="small">For talent and recruitment matters,<br>anna@brightlarkagency.sg<br>For marketing, media and account<br>matters,<br>leon@brightlarkagency.sg</p>
  </div>
  <div class="rules" style="top:340px;left:0;right:auto;width:225px"></div>
  <div class="rules" style="top:340px;left:361px"></div>
  <div class="logo">BRIGHT<br>LARK<br>AGENCY</div>
  <div class="social social--one"><span class="social__dot"></span><span>Like Us on<br>Pagebook</span></div>
  <div class="social social--two"><span class="social__dot"></span><span>Follow Us on<br>Chirper</span></div>
  <div class="social social--three"><span class="social__dot"></span><span>Subscribe on<br>ViewTube</span></div>
</section>

</body>
</html>
```